Quantel Brightforge/Innovation Consultant-One Page (for now) Site Reflective Of Its Focus.

Based in Tampa, Florida...I offer my consulting services, along with my extensive network of companies and technologies, to people that are looking for new, novel, and innovative applications for their technology and/or companies & governmental agencies to identify solutions to their Existing Challenges and Future Needs. I then Identify Connections and/or Solutions between technologies and set up collaborations between the parties. I also run a Forum that allows people to present new, novel, and innovative technologies and capabilities to a broad audience for ideation and collaboration.

Logo Text

Quantel Brightforge LLC

Coding

Coded - Design and coding required

```html
<!DOCTYPE html>
<html lang="en">
<head>
<meta charset="utf-8">
<title>Quantel Brightforge LLC</title>
<link href="https://fonts.googleapis.com/css2?family=Roboto:wght@400;500;700&display=swap" rel="stylesheet">
<style>
:root{
  --blue:#0a6dc0;
  --blue-dark:#075a9f;
  --gold:#fbb614;
  --ink:#1d1d1d;
  --muted:#7a7a7a;
  --cream:#fdf9eb;
  --white:#fff;
}
*{box-sizing:border-box;margin:0;padding:0}
html,body{width:1200px;height:4195px;overflow:hidden}
body{font-family:'Roboto',sans-serif;color:var(--ink);background:var(--white);position:relative}
svg{display:block}
.btn{position:absolute;background:var(--gold);color:#fff;font-weight:700;font-size:13px;text-transform:uppercase;display:flex;align-items:center;justify-content:center;gap:7px;letter-spacing:.2px}
.btn .dot{width:11px;height:11px;border-radius:50%;background:#fff;position:relative}
.btn .dot::after{content:"";position:absolute;left:4px;top:3px;border-left:4px solid var(--gold);border-top:2.5px solid transparent;border-bottom:2.5px solid transparent}
.heading{position:absolute;left:0;width:1200px;text-align:center;color:var(--blue);font-weight:700;font-size:38px}
.underline{position:absolute;height:3px;width:74px;background:var(--gold)}

/* top bar */
.topbar{position:absolute;top:0;left:0;width:1200px;height:41px;background:var(--blue);color:#fff;font-size:13px}
.topbar .item{position:absolute;top:12px;display:flex;align-items:center;gap:8px}
.social-top{position:absolute;top:13px;right:110px;display:flex;gap:20px}
.social-top span{width:12px;height:12px;border-radius:50%;background:#fff;display:block}

/* header */
.header{position:absolute;top:41px;left:0;width:1200px;height:109px;background:#fff;z-index:3}
.logo-tab{position:absolute;left:76px;top:41px;width:157px;height:151px;background:#fff;clip-path:polygon(0 0,100% 0,100% 72%,85% 100%,15% 100%,0 72%);z-index:4;display:flex;flex-direction:column;align-items:center;justify-content:center;padding-bottom:28px}
.logo-tab .mark{width:54px;height:54px;background:var(--blue);margin-bottom:8px}
.logo-tab .name{font-size:9px;font-weight:700;color:var(--ink);text-align:center;line-height:1.2}
.nav{position:absolute;top:48px;left:402px;display:flex;gap:29px;font-size:13px;font-weight:500;text-transform:uppercase}
.nav .active{color:var(--gold)}

/* hero */
.hero{position:absolute;top:150px;left:0;width:1200px;height:566px;background:linear-gradient(100deg,#2a3140 0%,#3b4454 35%,#5a4c40 60%,#2c3544 100%)}
.hero .glow{position:absolute;left:820px;top:120px;width:320px;height:320px;border-radius:50%;background:radial-gradient(circle,rgba(255,190,120,.55),rgba(255,150,60,0) 70%)}
.hero .welcome{position:absolute;left:111px;top:168px;color:#fff;font-weight:500;font-size:22px}
.hero h1{position:absolute;left:111px;top:200px;color:#fff;font-weight:700;font-size:37px}
.hero p{position:absolute;left:111px;top:264px;width:490px;color:#fff;font-size:16px;font-weight:500;line-height:27px}
.hero-dots{position:absolute;left:996px;top:525px;display:flex;gap:22px;align-items:center}
.hero-dots span{width:6px;height:6px;border-radius:50%;background:#fff}
.hero-dots .on{width:14px;height:14px;border:2px solid #fff;background:var(--blue)}

/* solutions */
.sol-card{position:absolute;top:923px;width:306px;height:368px;background:#fff;box-shadow:0 4px 18px rgba(0,0,0,.12);text-align:center}
.sol-card.active{border:3px solid var(--gold)}
.sol-card .icon{width:90px;height:90px;border-radius:50%;background:var(--blue);margin:38px auto 0}
.sol-card.active .icon{background:var(--gold);margin-top:35px}
.sol-card h3{margin-top:26px;color:var(--blue);font-size:17px;font-weight:700;line-height:28px}
.sol-card .bar{width:38px;height:2px;background:var(--gold);margin:12px auto 0}
.sol-card p{margin:17px auto 0;width:252px;font-size:14.5px;line-height:25.5px;color:var(--muted)}

/* about */
.about{position:absolute;top:1433px;left:0;width:1200px;height:591px;background:var(--cream)}
.about .frame{position:absolute;left:111px;top:353px;width:167px;height:164px;border:3px solid var(--blue)}
.about .dots{position:absolute;left:488px;top:73px}
.about .photo{position:absolute;left:147px;top:109px;width:426px;height:374px;border:4px solid #fff;background:linear-gradient(135deg,#e9ecef,#bfc6cf 55%,#7b8794);box-shadow:0 4px 14px rgba(0,0,0,.15)}
.about h2{position:absolute;left:663px;top:114px;color:var(--blue);font-size:38px;font-weight:700}
.about p{position:absolute;left:663px;top:198px;width:426px;font-size:14.5px;line-height:26.6px;color:var(--muted);text-align:justify}

/* blog */
.post{position:absolute;top:2253px;width:309px;height:360px}
.post .img{position:absolute;left:0;top:0;width:309px;height:223px}
.post .box{position:absolute;left:0;top:190px;width:288px;height:168px;background:#fff;border-bottom:4px solid var(--gold);padding:16px 17px}
.post .date{font-size:13px;color:var(--blue)}
.post h4{margin-top:9px;font-size:17px;font-weight:700;line-height:26px}
.post p{margin-top:8px;font-size:14px;line-height:22px;color:var(--muted);text-align:justify}

/* testimonials */
.testi{position:absolute;top:2743px;left:0;width:1200px;height:467px;overflow:hidden;background:linear-gradient(90deg,#f2f4f6 0%,#dfe3e7 45%,#9aa4ae 75%,#5b636c 100%)}
.testi .circle{position:absolute;left:78px;top:-40px;width:540px;height:540px;border-radius:50%;background:rgba(238,243,248,.92)}
.testi h2{position:absolute;left:184px;top:66px;color:var(--blue);font-size:38px;font-weight:700}
.testi q{position:absolute;left:184px;top:150px;width:345px;font-size:14px;line-height:26px;color:var(--muted);quotes:"\201C" "\201D"}
.testi .who{position:absolute;left:184px;top:284px;font-size:17px;color:var(--blue);font-weight:500}
.testi .who small{font-size:13px;color:var(--ink);font-weight:400}

/* contact */
.info{position:absolute;top:3413px;display:flex;gap:28px}
.info .ic{width:62px;height:62px;border-radius:50%;background:var(--blue);display:flex;align-items:center;justify-content:center;flex-shrink:0}
.info h5{font-size:13px;font-weight:700;margin-top:11px}
.info span{display:block;font-size:13px;color:var(--muted);margin-top:9px;line-height:20px}
.field{position:absolute;background:#fff;box-shadow:0 2px 10px rgba(0,0,0,.1);font-size:14px;color:#666;padding:17px 17px}

/* footer */
.footer{position:absolute;top:3834px;left:0;width:1200px;height:361px;background:var(--blue);color:#fff}
.footer h6{position:absolute;top:69px;font-size:17px;font-weight:700;text-transform:uppercase}
.footer .list{position:absolute;top:111px;font-size:14px;line-height:20px}
.footer .list div{display:flex;gap:14px;margin-bottom:17px;align-items:flex-start}
.footer .divider{position:absolute;left:405px;top:68px;width:1px;height:165px;background:rgba(255,255,255,.3)}
.footer .links{position:absolute;top:111px;font-size:14px}
.footer .links div{display:flex;gap:14px;align-items:center;margin-bottom:16px}
.footer .links i{width:12px;height:12px;border-radius:50%;background:var(--gold);display:block}
.sub{position:absolute;left:804px;top:112px;width:283px;height:48px;background:#fff;display:flex}
.sub span{flex:1;color:#666;font-size:14px;padding:17px 18px}
.sub b{width:45px;margin:3px;background:var(--gold)}
.f-social{position:absolute;left:806px;top:174px;display:flex;gap:6px}
.f-social span{width:33px;height:33px;border-radius:50%;border:2px solid #fff}
.f-social span:first-child{background:var(--gold);border-color:var(--gold)}
.footer .rule{position:absolute;left:111px;top:298px;width:977px;height:1px;background:rgba(255,255,255,.3)}
.footer .copy{position:absolute;top:318px;left:0;width:1200px;text-align:center;font-size:13px}
</style>
</head>
<body>

<div class="topbar">
  <div class="item" style="left:111px">
    <svg width="12" height="12" viewBox="0 0 24 24"><path fill="#fbb614" d="M6.6 10.8a15 15 0 0 0 6.6 6.6l2.2-2.2c.3-.3.7-.4 1-.2 1.1.4 2.3.6 3.6.6.6 0 1 .4 1 1V20c0 .6-.4 1-1 1A17 17 0 0 1 3 4c0-.6.4-1 1-1h3.5c.6 0 1 .4 1 1 0 1.3.2 2.5.6 3.6.1.3 0 .7-.2 1z"/></svg>
    +1 (555) 014 2288 <span style="margin-left:14px">|</span>
  </div>
  <div class="item" style="left:282px">
    <svg width="13" height="10" viewBox="0 0 26 20"><rect width="26" height="20" rx="2" fill="#fbb614"/><path d="M1 2l12 9 12-9" stroke="#0a6dc0" stroke-width="2" fill="none"/></svg>
    info@quantelbrightforge.net
  </div>
  <div class="social-top" aria-label="Social links"><span></span><span></span><span></span><span></span></div>
</div>

<div class="header">
  <nav class="nav">
    <span class="active">Home</span><span>About Us</span><span>Solutions</span><span>Blog</span><span>Contact Us &nbsp;&nbsp;|</span>
    <svg width="13" height="13" viewBox="0 0 24 24" style="margin-left:-10px;margin-top:1px"><circle cx="10" cy="10" r="7" stroke="#1d1d1d" stroke-width="3" fill="none"/><path d="M15 15l7 7" stroke="#1d1d1d" stroke-width="3"/></svg>
  </nav>
  <div class="btn" style="left:928px;top:31px;width:160px;height:48px">Request a Quote</div>
</div>
<div class="logo-tab"><div class="mark"></div><div class="name">Quantel Brightforge LLC</div></div>

<section class="hero" role="img" aria-label="Hand holding a glowing light bulb with cloud and business icons connected by circuit lines">
  <div class="glow"></div>
  <div class="welcome">WELCOME TO</div>
  <h1>QUANTEL BRIGHTFORGE</h1>
  <p>Lorem ipsum dolor sit amet, consectetur adipiscing elit, sed do eiusmod tempor incididunt ut labore et dolore magna aliqua utenim ad minim veniam, quis nostrud.</p>
  <div class="btn" style="left:111px;top:366px;width:143px;height:47px">Get Started <span class="dot"></span></div>
  <div class="hero-dots"><span></span><span class="on"></span><span></span><span></span></div>
</section>

<h2 class="heading" style="top:818px">OUR SOLUTIONS</h2>
<div class="underline" style="left:563px;top:870px"></div>

<div class="sol-card" style="left:111px"><div class="icon" role="img" aria-label="Growth chart in hand icon"></div><h3>LOREM IPSUM DOLOR<br>SIT AMET SED</h3><div class="bar"></div><p>Sed ut perspiciatis unde omnis iste natus error sit voluptatem accus an tium doloremque laudantium, totam apemque laudantira.</p></div>
<div class="sol-card active" style="left:446px"><div class="icon" role="img" aria-label="Idea gears icon"></div><h3>LOREM IPSUM DOLOR<br>SIT AMET SED</h3><div class="bar"></div><p>Sed ut perspiciatis unde omnis iste natus error sit voluptatem accus an tium doloremque laudantium, totam apemque laudantira.</p></div>
<div class="sol-card" style="left:783px"><div class="icon" role="img" aria-label="Team in hands icon"></div><h3>LOREM IPSUM DOLOR<br>SIT AMET SED</h3><div class="bar"></div><p>Sed ut perspiciatis unde omnis iste natus error sit voluptatem accus an tium doloremque laudantium, totam apemque laudantira.</p></div>

<section class="about">
  <div class="frame"></div>
  <svg class="dots" width="122" height="122" viewBox="0 0 122 122">
    <defs><pattern id="dp" width="12" height="12" patternUnits="userSpaceOnUse"><circle cx="3" cy="3" r="1.8" fill="#c9c9c9"/></pattern></defs>
    <rect width="122" height="122" fill="url(#dp)"/>
  </svg>
  <div class="photo" role="img" aria-label="Smiling woman in glasses seated at a desk with a laptop"></div>
  <h2>ABOUT US</h2>
  <div class="underline" style="left:663px;top:162px"></div>
  <p>Lorem ipsum dolor sit amet, consectetur adipiscing elit, sed do eiusmod tempor incididunt ut labore et dolore magna aliqua. Ut enim ad minim veniam, quis nostrud exercitation ullamco laboris nisi ut aliquip ex ea commodo consequat. Duis aute irure dolor in reprehenderit in voluptate velit esse cillum dolore eu fugiat nulla pariatur excepteur sint occaecat cupidatat non proident, sunt in culpea.</p>
  <div class="btn" style="left:663px;top:420px;width:141px;height:48px">Learn More <span class="dot"></span></div>
</section>

<h2 class="heading" style="top:2141px">LATEST BLOG POSTS</h2>
<div class="underline" style="left:557px;top:2193px"></div>

<article class="post" style="left:111px"><div class="img" role="img" aria-label="Woman touching a holographic screen" style="background:linear-gradient(120deg,#2b3038,#5c6470 60%,#8fb2cf)"></div><div class="box"><div class="date">27 Jun 2023</div><h4>Lorem ipsum dolor sit ame consectetur adipea</h4><p>Sed ut perspiciatis unde omnis iste natus err tatem accusea...</p></div></article>
<article class="post" style="left:446px"><div class="img" role="img" aria-label="Glowing bulb inside a digital brain network" style="background:radial-gradient(circle at 50% 45%,#c89a64,#2a2f36 45%,#15181d)"></div><div class="box"><div class="date">27 Jun 2023</div><h4>Lorem ipsum dolor sit ame consectetur adipea</h4><p>Sed ut perspiciatis unde omnis iste natus err tatem accusea...</p></div></article>
<article class="post" style="left:780px"><div class="img" role="img" aria-label="Team working together at computers in an office" style="background:linear-gradient(120deg,#2d3a4e,#4a5b72 50%,#6b7d95)"></div><div class="box"><div class="date">27 Jun 2023</div><h4>Lorem ipsum dolor sit ame consectetur adipea</h4><p>Sed ut perspiciatis unde omnis iste natus err tatem accusea...</p></div></article>

<section class="testi" role="img" aria-label="Smiling man in glasses typing on a laptop in a bright office">
  <div class="circle"></div>
  <h2>TESTIMONIALS</h2>
  <div class="underline" style="left:184px;top:114px"></div>
  <q>Lorem ipsum dolor sit amet, consectetur adipis cing elit sed do eiusmod tempor incididunt ut labore et dolore magna aliqua. Ut enim ad minim veniam, quis nostrud exercitation ullamco laboris nisi ut aliquip ex ea commodo coincididunt ut nsea.</q>
  <div class="who">Marcus Delane, <small>Florida</small></div>
  <div class="btn" style="left:184px;top:337px;width:181px;height:48px">View All Reviews <span class="dot"></span></div>
</section>

<h2 class="heading" style="top:3315px">GET IN TOUCH</h2>
<div class="underline" style="left:563px;top:3366px"></div>

<div class="info" style="left:156px">
  <div class="ic"><svg width="22" height="24" viewBox="0 0 22 24"><path d="M11 1a7 7 0 0 0-7 7c0 5 7 11 7 11s7-6 7-11a7 7 0 0 0-7-7z" fill="none" stroke="#fff" stroke-width="2"/><circle cx="11" cy="8" r="2.5" fill="#fff"/><ellipse cx="11" cy="21" rx="9" ry="2" fill="none" stroke="#fff" stroke-width="1.5"/></svg></div>
  <div><h5>LOCATION:</h5><span>465, Lorum Ipsum Dolore,<br>Tampa, Florida</span></div>
</div>
<div class="info" style="left:466px">
  <div class="ic"><svg width="22" height="22" viewBox="0 0 24 24"><path fill="#fff" d="M6.6 10.8a15 15 0 0 0 6.6 6.6l2.2-2.2c.3-.3.7-.4 1-.2 1.1.4 2.3.6 3.6.6.6 0 1 .4 1 1V20c0 .6-.4 1-1 1A17 17 0 0 1 3 4c0-.6.4-1 1-1h3.5c.6 0 1 .4 1 1 0 1.3.2 2.5.6 3.6.1.3 0 .7-.2 1z"/></svg></div>
  <div><h5>PHONE:</h5><span>+1 (555) 014 2288</span></div>
</div>
<div class="info" style="left:738px">
  <div class="ic"><svg width="24" height="18" viewBox="0 0 26 20"><rect x="1" y="1" width="24" height="18" rx="2" fill="none" stroke="#fff" stroke-width="2"/><path d="M1 2l12 9 12-9" stroke="#fff" stroke-width="2" fill="none"/></svg></div>
  <div><h5>EMAIL ADDRESS:</h5><span>info@quantelbrightforge.net</span></div>
</div>

<div class="field" style="left:166px;top:3513px;width:281px;height:49px">Full Name</div>
<div class="field" style="left:459px;top:3513px;width:282px;height:49px">Phone Number</div>
<div class="field" style="left:752px;top:3513px;width:282px;height:49px">Email Address</div>
<div class="field" style="left:166px;top:3575px;width:868px;height:93px">Message...!</div>
<div class="btn" style="left:518px;top:3686px;width:162px;height:49px;font-size:14px">Send Message</div>

<footer class="footer">
  <h6 style="left:111px">Contact Us</h6>
  <div class="list" style="left:111px;width:260px">
    <div><svg width="11" height="14" viewBox="0 0 22 28" style="margin-top:3px;flex-shrink:0"><path d="M11 1a10 10 0 0 0-10 10c0 7 10 16 10 16s10-9 10-16A10 10 0 0 0 11 1z" fill="#fbb614"/></svg><span>465, Lorum Ipsum Dolore Sed,<br>Tampa, Florida</span></div>
    <div><svg width="12" height="12" viewBox="0 0 24 24" style="margin-top:3px;flex-shrink:0"><path fill="#fbb614" d="M6.6 10.8a15 15 0 0 0 6.6 6.6l2.2-2.2c.3-.3.7-.4 1-.2 1.1.4 2.3.6 3.6.6.6 0 1 .4 1 1V20c0 .6-.4 1-1 1A17 17 0 0 1 3 4c0-.6.4-1 1-1h3.5c.6 0 1 .4 1 1 0 1.3.2 2.5.6 3.6.1.3 0 .7-.2 1z"/></svg><span>+1 (555) 014 2288</span></div>
    <div><svg width="13" height="10" viewBox="0 0 26 20" style="margin-top:5px;flex-shrink:0"><rect width="26" height="20" rx="2" fill="#fbb614"/><path d="M1 2l12 9 12-9" stroke="#0a6dc0" stroke-width="2" fill="none"/></svg><span>info@quantelbrightforge.net</span></div>
  </div>
  <div class="divider"></div>
  <h6 style="left:456px">Links</h6>
  <div class="links" style="left:456px"><div><i></i>Home</div><div><i></i>About Us</div><div><i></i>Solutions</div><div><i></i>Blog</div><div><i></i>Contact Us</div></div>
  <div class="links" style="left:620px"><div><i></i>FAQ</div><div><i></i>Site Map</div><div><i></i>Privacy Policy</div><div><i></i>Terms Of Use</div></div>
  <h6 style="left:804px">Subscribe for Updates</h6>
  <div class="sub"><span>Email Address</span><b></b></div>
  <div class="f-social" aria-label="Social links"><span></span><span></span><span></span><span></span></div>
  <div class="rule"></div>
  <div class="copy">© 2023 <b>QUANTEL BRIGHTFORGE</b> &nbsp;|&nbsp; All Rights Reserved</div>
</footer>

</body>
</html>
```